Redesign of Plastic Surgeon Website to fully responsive / modern feel

Hi

Our current website is out of date www.harbourlinecosmetic.org

We want a fresh / modern looking design
Needs to be fully responsive design that works extremely well on ipad and mobile device

Would like design for both full screen website and mobile

Have listed a few websites of other plastic surgeons we like
http://www.reformclinicdaily.com/
http://www.peterholtbymd.com/
http://www.corvanbeauty.com/
http://www.tidewellcontouring.com/

Menu needs to include
1. About Us
2. Procedures (see current website for example)
3. News
4. Patient Resources
5. Contact Us

We are flexible with colours / images / layout

I have uploaded a document that has some content - the face pages content is completed only

some of the procedures can have content upwards of 4000 words - total website can be large with over 40,000 words
Updates

Target Market(s)

Mainly women 20-60 85% of practice
Some men 15%

Industry/Entity Type

Plastic Surgery

Number of Pages Required

5+ page

Requirements
Must have
• We need designs for
• Homepage
• Internal pages
• 1. Landing pages for breast / body / face / non surgical main pages
• 2. Procedure pages for individual pages under each section - eg breast augmentation
• 3. About us pages - like meet the doctor, our staff, clinics
• 4. Contact page
• 5. Blog / News page
Nice to have
• See our list of websites for examples of designs we like
• Like full screen design with nice hero image
• Needs to have good to call to action messages on home page like
• Specials, procedure of the month, etc

```html
<!DOCTYPE html>
<html lang="en">
<head>
<meta charset="utf-8">
<title>Harbourline Cosmetic Institute</title>
<link rel="stylesheet" href="https://fonts.googleapis.com/css2?family=Lato:ital,wght@0,300;0,400;0,700;0,900;1,400&family=Oswald:wght@500&display=swap">
<style>
:root{
  --ink:#333333;
  --muted:#777777;
  --red:#e8505b;
  --dark:#3b3b3b;
  --nav:#a39d98;
  --nav-active:#3b3b3b;
  --soft:#f3f3f3;
  --purple:#b552c9;
  --teal:#21c6d3;
  --orange:#f5a623;
  --sky:#5cb3cb;
  --yellow:#f7c41f;
  --green:#5cc86a;
  --blue:#2aa7e0;
  --white:#ffffff;
}
*{box-sizing:border-box;margin:0;padding:0}
html,body{width:1200px;height:2273px;overflow:hidden}
body{font-family:"Lato",Arial,sans-serif;color:var(--ink);background:var(--white);position:relative}
.abs{position:absolute}
a{color:inherit;text-decoration:none}
.read-more{font-size:10px;font-weight:700;letter-spacing:.5px;text-transform:uppercase;display:flex;align-items:center;gap:5px}
.read-more::before{content:"";width:8px;height:8px;border-radius:50%;background:currentColor;display:inline-block}
.rule{height:2px;background:var(--red)}

/* header */
.header{left:0;top:0;width:1200px;height:71px;background:var(--white)}
.brand{left:208px;top:0;width:113px;height:176px;background:#4a4a4a;clip-path:polygon(0 0,100% 0,100% 100%,50% 90%,0 100%);z-index:5;display:flex;align-items:flex-start;justify-content:center;padding-top:24px}
.brand-name{color:var(--white);font-weight:400;font-size:11.5px;line-height:18px;letter-spacing:1px;text-transform:uppercase;text-align:center;white-space:nowrap}
.booking{left:660px;top:16px;text-align:right;width:230px}
.booking small{display:block;font-size:11px;color:var(--ink);padding-right:60px}
.booking .phone{font-size:17px;color:var(--red);display:flex;justify-content:flex-end;align-items:center;gap:6px;margin-top:4px}
.social{display:flex;gap:4px}
.social span{width:20px;height:20px;border-radius:50%;display:block}
.social-top{left:901px;top:24px}
.nav{left:0;top:71px;width:1200px;height:27px;background:var(--nav)}
.nav ul{list-style:none;position:absolute;left:414px;top:0;display:flex;height:27px}
.nav li{font-size:9.5px;color:var(--white);letter-spacing:.4px;text-transform:uppercase;line-height:27px;text-align:center;white-space:nowrap}
.nav li.active{background:var(--nav-active)}
.nav .search{position:absolute;left:984px;top:9px}

/* hero */
.hero{left:0;top:98px;width:1200px;height:394px;background:linear-gradient(90deg,#e4ebe8 0%,#dfe8e5 45%,#c9dfdb 100%)}
.hero-photo{left:560px;top:98px;width:500px;height:394px;background:radial-gradient(ellipse at 60% 40%,#f3d5c6 0%,#e2bfae 35%,#cfd9d4 75%,transparent 100%)}
.hero-title{left:208px;top:257px;font-weight:300;font-size:26px;line-height:30px;color:#555}
.hero-title span{display:block;font-size:20px;line-height:26px}
.hero-rule{left:208px;top:322px;width:112px}
.hero-more{left:208px;top:341px;color:#444}
.arrow{top:283px}
.band{left:0;top:492px;width:1200px;height:199px;background:var(--dark)}

/* cards */
.card{top:439px;width:247px;height:194px;background:var(--white);box-shadow:0 2px 6px rgba(0,0,0,.2)}
.card-head{height:56px;background:#f4f4f4;padding:14px 22px;font-weight:900;font-size:24px;letter-spacing:.5px;text-transform:uppercase}
.card-img{height:138px}
.card.face{left:208px;border-top:6px solid var(--purple)}
.card.body{left:476px;border-top:6px solid var(--teal);padding:12px 28px}
.card.breast{left:744px;border-top:6px solid var(--orange)}
.body-title{font-weight:900;font-size:24px;color:var(--teal);text-transform:uppercase}
.body-sub{font-size:16px;margin-top:2px}
.body .rule{width:72px;margin:10px 0 14px}
.body ul{list-style:none;font-size:10px;color:#666;line-height:17px}
.body li::before{content:"›";margin-right:6px}
.body .read-more{color:var(--red);margin-top:26px}

/* doctor */
.doctor{left:0;top:691px;width:1200px;height:344px;background:var(--soft)}
.doctor-photo{left:252px;top:674px;width:234px;height:361px;background:linear-gradient(180deg,#dcdcdc 0%,#eef2f6 30%,#e1e8ef 100%);border-radius:110px 110px 0 0}
.doctor-name{left:544px;top:740px;font-weight:300;font-size:26px}
.doctor-role{left:544px;top:772px;font-size:11px;color:var(--red)}
.doctor-bio{left:544px;top:802px;width:380px;font-size:10.5px;line-height:16px;color:#666}
.doctor-more{left:544px;top:902px;color:#444}
.like{left:544px;top:951px;width:184px;height:24px;background:var(--white);border:1px solid #ddd;box-shadow:1px 1px 2px rgba(0,0,0,.15);display:flex;align-items:center;font-size:10px;color:#3b5998}
.like i{width:22px;height:22px;background:#3b5998;margin-right:8px;display:block}

/* features */
.col-title{top:1088px;font-weight:700;font-size:17px}
.col-rule{top:1115px;width:112px}
.quote{left:208px;top:1138px;width:215px;font-style:italic;font-size:11.5px;line-height:16px;color:#444}
.story{left:208px;top:1205px;color:var(--red);font-size:10px;text-transform:none;letter-spacing:0;font-weight:400}
.thumbs{left:208px;top:1250px;display:flex;gap:5px}
.thumbs span{width:28px;height:28px;background:linear-gradient(135deg,#d9c4b8,#a48c7e);display:block}
.thumbs span.on{border-bottom:3px solid var(--red);height:34px}
.gallery{left:476px;top:1141px;width:201px;height:146px;display:flex;gap:2px}
.gallery div{flex:1;background:linear-gradient(180deg,#6f7478,#a0897c 60%,#7b6a60);position:relative}
.gallery b{position:absolute;left:0;right:0;bottom:0;height:17px;background:rgba(40,40,40,.75);color:var(--white);font-size:10px;font-weight:400;padding:3px 6px}
.video{left:744px;top:1141px;width:201px;height:146px;background:linear-gradient(135deg,#e8ebee,#c7d0dc 60%,#8fa5d6)}
.play{left:829px;top:1199px;width:30px;height:30px;border-radius:50%;background:#333;display:flex;align-items:center;justify-content:center}
.seal{width:74px;height:74px}
.seal text{font-family:"Lato",Arial,sans-serif;font-style:italic;font-size:11px;fill:#fff;text-anchor:middle}

/* cta */
.cta{left:0;top:1341px;width:1200px;height:201px;background:var(--sky);text-align:center;color:var(--white)}
.cta h2{font-weight:400;font-size:25px;margin-top:53px}
.cta p{font-size:12px;font-weight:700;margin-top:2px}
.cta-btn{display:inline-flex;align-items:center;gap:5px;margin-top:13px;background:var(--yellow);color:#333;font-size:15px;padding:5px 14px;box-shadow:0 2px 0 #c99a0c}

/* news */
.news-title{left:208px;top:1597px;font-weight:700;font-size:17px}
.news-rule{left:208px;top:1625px;width:112px}
.news-card{top:1651px;width:180px;height:304px;background:linear-gradient(180deg,#fff 0%,#f5f5f5 100%)}
.news-img{height:106px;background:linear-gradient(135deg,#eef1f3,#c9d6df 55%,#e4c7b4)}
.news-card .bar{height:3px}
.news-body{padding:14px 17px}
.news-body h3{font-weight:400;font-size:12px;line-height:15px}
.tag{font-size:9px;margin-top:12px;display:flex;align-items:center;gap:5px;color:#333}
.news-body p{font-size:10px;line-height:14px;color:#777;margin-top:14px}
.news-body .read-more{margin-top:30px;font-size:8.5px;color:#333}
.date{right:-14px;top:-14px;width:44px;height:44px}
.date text{font-family:"Lato",Arial,sans-serif;font-size:15px;fill:#fff;text-anchor:middle}

/* signup */
.signup{left:0;top:2000px;width:1200px;height:121px;background:var(--dark)}
.signup-badge{left:258px;top:1966px;width:188px;height:188px}
.signup-title{left:465px;top:2016px;font-weight:300;font-size:25px;color:var(--white)}
.signup-sub{left:465px;top:2044px;font-size:12px;color:var(--white)}
.signup-form{left:465px;top:2072px;display:flex}
.signup-form span{width:181px;height:27px;border:1px solid #666;font-size:10px;color:#ccc;padding:7px 8px}
.signup-form b{width:97px;height:27px;background:var(--red);color:var(--white);font-weight:400;font-size:11px;text-align:center;line-height:27px}

/* footer */
.footer{left:0;top:2121px;width:1200px;height:152px;background:var(--soft)}
.footer-links{left:208px;top:2181px;font-size:10.5px;color:#333;word-spacing:2px}
.back-top{left:918px;top:2181px;font-size:10px;font-style:italic;color:#888;display:flex;gap:5px;align-items:center}
.footer-line{left:208px;top:2206px;width:784px;height:1px;background:#dedede}
.copyright{left:208px;top:2232px;font-size:10px;color:#666}
.social-bottom{left:901px;top:2228px}
</style>
</head>
<body>

<header class="abs header"></header>
<div class="abs brand"><span class="brand-name">Harbourline<br>Cosmetic<br>Institute</span></div>
<div class="abs booking">
  <small>Book your Appointments</small>
  <div class="phone">Call Us
    <svg width="16" height="16" viewBox="0 0 16 16"><circle cx="8" cy="8" r="7" fill="none" stroke="#e8505b" stroke-width="1.5"/><path d="M5.5 4.5l1.5 1.5-1 1c.5 1.2 1.4 2.1 2.6 2.6l1-1 1.5 1.5-1.2 1.2C7.6 11 5 8.4 4.3 5.7z" fill="#e8505b"/></svg>
    02 9170 4862</div>
</div>
<div class="abs social social-top"><span style="background:#3b5998"></span><span style="background:#2aa3ef"></span><span style="background:#0e76a8"></span><span style="background:#dd4b39"></span></div>

<nav class="abs nav">
  <ul>
    <li class="active" style="width:72px">Home</li>
    <li style="width:80px">About Us</li>
    <li style="width:104px">Procedures</li>
    <li style="width:58px">News</li>
    <li style="width:144px">Patient Resources</li>
    <li style="width:92px">Contact Us</li>
  </ul>
  <svg class="search" width="10" height="10" viewBox="0 0 10 10"><circle cx="4" cy="4" r="3" fill="none" stroke="#fff" stroke-width="1.4"/><path d="M6.3 6.3L9 9" stroke="#fff" stroke-width="1.4"/></svg>
</nav>

<section class="abs hero"></section>
<div class="abs hero-photo" role="img" aria-label="Portrait of a woman with long dark hair and a white flower, touching her cheek"></div>
<h1 class="abs hero-title">Invest in yourself, renew your look<span>and refresh your confidence</span></h1>
<div class="abs rule hero-rule"></div>
<a class="abs read-more hero-more">Read More</a>
<svg class="abs arrow" style="left:152px" width="14" height="26" viewBox="0 0 14 26"><path d="M12 2L2 13l10 11" fill="none" stroke="#fff" stroke-width="2"/></svg>
<svg class="abs arrow" style="left:1026px" width="14" height="26" viewBox="0 0 14 26"><path d="M2 2l10 11L2 24" fill="none" stroke="#fff" stroke-width="2"/></svg>

<div class="abs band"></div>

<article class="abs card face">
  <div class="card-head">Face</div>
  <div class="card-img" role="img" aria-label="Woman with long brown hair, facial procedures" style="background:linear-gradient(135deg,#f1ded2,#b98a72 55%,#6e4a3a)"></div>
</article>
<article class="abs card body">
  <div class="body-title">Body</div>
  <div class="body-sub">Surgery Reviews</div>
  <div class="rule"></div>
  <ul><li>Tummy Tuck</li><li>Liposuction</li><li>Brachioplasty</li></ul>
  <a class="read-more">Read More</a>
</article>
<article class="abs card breast">
  <div class="card-head">Breast</div>
  <div class="card-img" role="img" aria-label="Woman's torso, breast procedures" style="background:linear-gradient(135deg,#fbf1ea,#f0cfbc 55%,#e3b69c)"></div>
</article>

<section class="abs doctor"></section>
<div class="abs doctor-photo" role="img" aria-label="Smiling surgeon in a white coat with a stethoscope"></div>
<h2 class="abs doctor-name">Dr Graham Whitcombe</h2>
<div class="abs doctor-role">(Cosmetic Surgery Harbourline)</div>
<p class="abs doctor-bio">I started life as the only boy in a family of six children. We had a pretty spartan upbringing, but my single mother worked at menial jobs to ensure we all got a professional education. Inspired by an uncle who was a surgeon, I chose to become a doctor. Early on at medical school, I found myself to be dexterous of hand, so surgery was my</p>
<a class="abs read-more doctor-more">Read More</a>
<div class="abs like"><i></i>Like Dr Graham R. Whitcombe</div>

<h3 class="abs col-title" style="left:208px">Real patients</h3>
<div class="abs rule col-rule" style="left:208px"></div>
<p class="abs quote">“I'm just your basic Midwestern housewife...Well, maybe not so basic anymore.”</p>
<a class="abs read-more story">Read Melissa's Story</a>
<div class="abs thumbs"><span></span><span class="on"></span><span></span><span></span><span></span><span></span></div>

<h3 class="abs col-title" style="left:476px">Photo Gallery</h3>
<div class="abs rule col-rule" style="left:476px"></div>
<div class="abs gallery" role="img" aria-label="Before and after facelift photos of a blonde woman">
  <div><b>Before</b></div><div><b>After</b></div>
</div>
<svg class="abs seal" style="left:641px;top:1103px" viewBox="0 0 74 74"><polygon points="37,1 43,7 51,4 54,12 62,12 62,20 70,23 67,31 73,37 67,43 70,51 62,54 62,62 54,62 51,70 43,67 37,73 31,67 23,70 20,62 12,62 12,54 4,51 7,43 1,37 7,31 4,23 12,20 12,12 20,12 23,4 31,7" fill="#f5a623"/><circle cx="37" cy="37" r="26" fill="none" stroke="#fff" stroke-dasharray="2 2"/><text x="37" y="35">View</text><text x="37" y="48">Gallery</text></svg>

<h3 class="abs col-title" style="left:744px">Instructional Videos</h3>
<div class="abs rule col-rule" style="left:744px"></div>
<div class="abs video" role="img" aria-label="Video still of a patient's face being marked by gloved hands"></div>
<div class="abs play"><svg width="12" height="12" viewBox="0 0 12 12"><path d="M3 1l8 5-8 5z" fill="#fff"/></svg></div>
<svg class="abs seal" style="left:907px;top:1103px" viewBox="0 0 74 74"><polygon points="37,1 43,7 51,4 54,12 62,12 62,20 70,23 67,31 73,37 67,43 70,51 62,54 62,62 54,62 51,70 43,67 37,73 31,67 23,70 20,62 12,62 12,54 4,51 7,43 1,37 7,31 4,23 12,20 12,12 20,12 23,4 31,7" fill="#2bb8c0"/><circle cx="37" cy="37" r="26" fill="none" stroke="#fff" stroke-dasharray="2 2"/><text x="37" y="35">View</text><text x="37" y="48">Gallery</text></svg>

<section class="abs cta">
  <h2>Book Your Free Consultation with Our Nurse</h2>
  <p>at Lanecove Rooms (7 days a week from 8:00 am to 2:00 am)</p>
  <div class="cta-btn">Call Us
    <svg width="16" height="16" viewBox="0 0 16 16"><circle cx="8" cy="8" r="7" fill="none" stroke="#333" stroke-width="1.5"/><path d="M5.5 4.5l1.5 1.5-1 1c.5 1.2 1.4 2.1 2.6 2.6l1-1 1.5 1.5-1.2 1.2C7.6 11 5 8.4 4.3 5.7z" fill="#333"/></svg>
    (02) 9170 - 4862</div>
</section>

<h3 class="abs news-title">Latest News</h3>
<div class="abs rule news-rule"></div>

<article class="abs news-card" style="left:208px">
  <div class="news-img" role="img" aria-label="Two women examining skin in a mirror"></div>
  <div class="bar" style="background:var(--red)"></div>
  <div class="news-body"><h3 style="color:var(--red)">Lorem Ipsum is simply dummy text.</h3>
  <div class="tag"><svg width="9" height="9" viewBox="0 0 9 9"><path d="M0 0h4l5 5-4 4-5-5z" fill="#333"/></svg>Skin Care</div>
  <p>Nothing makes us look better than a smile coupled with gorgeous, healthy skin. The importance of good skincare becomes ....</p>
  <a class="read-more">Read More</a></div>
  <svg class="abs date" viewBox="0 0 36 36"><polygon points="18,0 22,4 28,3 29,8 34,11 32,16 36,20 32,23 33,29 27,30 25,35 20,33 15,36 12,32 6,33 5,27 0,25 2,20 0,15 4,12 4,6 10,5 12,0" fill="#e8505b"/><text x="17" y="23">30<tspan font-size="7" dy="-5">th</tspan></text></svg>
</article>
<article class="abs news-card" style="left:410px">
  <div class="news-img" role="img" aria-label="Doctor consulting with a female patient"></div>
  <div class="bar" style="background:var(--yellow)"></div>
  <div class="news-body"><h3 style="color:#e2b20f">Lorem Ipsum is simply dummy text.</h3>
  <div class="tag"><svg width="9" height="9" viewBox="0 0 9 9"><path d="M0 0h4l5 5-4 4-5-5z" fill="#333"/></svg>Skin Care</div>
  <p>Nothing makes us look better than a smile coupled with gorgeous, healthy skin. The importance of good skincare becomes ....</p>
  <a class="read-more">Read More</a></div>
  <svg class="abs date" viewBox="0 0 36 36"><polygon points="18,0 22,4 28,3 29,8 34,11 32,16 36,20 32,23 33,29 27,30 25,35 20,33 15,36 12,32 6,33 5,27 0,25 2,20 0,15 4,12 4,6 10,5 12,0" fill="#f7c41f"/><text x="17" y="23">28<tspan font-size="7" dy="-5">th</tspan></text></svg>
</article>
<article class="abs news-card" style="left:611px">
  <div class="news-img" role="img" aria-label="Woman receiving a cosmetic injection"></div>
  <div class="bar" style="background:var(--green)"></div>
  <div class="news-body"><h3 style="color:var(--green)">Lorem Ipsum is simply dummy text.</h3>
  <div class="tag"><svg width="9" height="9" viewBox="0 0 9 9"><path d="M0 0h4l5 5-4 4-5-5z" fill="#333"/></svg>Skin Care</div>
  <p>Nothing makes us look better than a smile coupled with gorgeous, healthy skin. The importance of good skincare becomes ....</p>
  <a class="read-more">Read More</a></div>
  <svg class="abs date" viewBox="0 0 36 36"><polygon points="18,0 22,4 28,3 29,8 34,11 32,16 36,20 32,23 33,29 27,30 25,35 20,33 15,36 12,32 6,33 5,27 0,25 2,20 0,15 4,12 4,6 10,5 12,0" fill="#5cc86a"/><text x="17" y="23">03<tspan font-size="7" dy="-5">th</tspan></text></svg>
</article>
<article class="abs news-card" style="left:812px">
  <div class="news-img" role="img" aria-label="Doctor with a stethoscope beside a smiling patient"></div>
  <div class="bar" style="background:var(--blue)"></div>
  <div class="news-body"><h3 style="color:var(--blue)">Lorem Ipsum is simply dummy text.</h3>
  <div class="tag"><svg width="9" height="9" viewBox="0 0 9 9"><path d="M0 0h4l5 5-4 4-5-5z" fill="#333"/></svg>Skin Care</div>
  <p>Nothing makes us look better than a smile coupled with gorgeous, healthy skin. The importance of good skincare becomes ....</p>
  <a class="read-more">Read More</a></div>
  <svg class="abs date" viewBox="0 0 36 36"><polygon points="18,0 22,4 28,3 29,8 34,11 32,16 36,20 32,23 33,29 27,30 25,35 20,33 15,36 12,32 6,33 5,27 0,25 2,20 0,15 4,12 4,6 10,5 12,0" fill="#2aa7e0"/><text x="17" y="23">12<tspan font-size="7" dy="-5">th</tspan></text></svg>
</article>

<section class="abs signup"></section>
<svg class="abs signup-badge" viewBox="0 0 188 188">
  <polygon points="94,4 104,16 118,8 124,22 140,18 141,34 157,35 153,50 168,56 159,69 172,80 159,89 168,102 153,108 160,122 145,125 147,141 131,140 128,156 114,150 106,164 94,154 82,164 74,150 60,156 57,140 41,141 43,125 28,122 35,108 20,102 29,89 16,80 29,69 20,56 35,50 31,35 47,34 48,18 64,22 70,8 84,16" fill="#e8505b" transform="translate(0,10)"/>
  <g transform="rotate(-12 94 94)" fill="#fff" text-anchor="middle" font-family="Oswald, Arial, sans-serif">
    <text x="94" y="72" font-size="22">E-Blast</text>
    <text x="94" y="96" font-size="18">SIGN UP Here</text>
    <text x="94" y="116" font-size="12">to Receive Monthly</text>
    <text x="94" y="131" font-size="12">Coupons and</text>
    <text x="94" y="146" font-size="12">Specials!!</text>
  </g>
</svg>
<h2 class="abs signup-title">Harbourline Cosmetic Institute</h2>
<div class="abs signup-sub">Monthly Coupons and Insider Specials</div>
<div class="abs signup-form"><span>Name</span><span>Email</span><b>SIGN UP</b></div>

<footer class="abs footer"></footer>
<div class="abs footer-links">Privacy Policy &nbsp;| &nbsp; Privacy Policy &nbsp;| &nbsp; Site Map | Privacy Policy &nbsp;| &nbsp; Terms of Use</div>
<div class="abs back-top">Back to Top <svg width="10" height="10" viewBox="0 0 10 10"><path d="M5 1L1 6h2.5v3h3V6H9z" fill="#333"/></svg></div>
<div class="abs footer-line"></div>
<div class="abs copyright">Copyright © 2016 Harbourline Cosmetic Institute. All rights reserved.</div>
<div class="abs social social-bottom"><span style="background:#3b5998"></span><span style="background:#2aa3ef"></span><span style="background:#0e76a8"></span><span style="background:#dd4b39"></span></div>

</body>
</html>
```